UI/UX design for non-profit education/student success foundation website

Looking to work with a ui/ux designer that can provide an elegant, impactful and modern responsive design for a non-profit education/student success foundation website. The website will need to have a lot of visuals and elements with impactful statements. The responsive templates will later be parsed (this will be done by another developer) and converted to Concrete5 CMS templates. The organization likes bold colors with a modern sleek design. Typography is also key in titles and statements of interest. On-scroll visuals could be nice if it lends well to combining imagery and text. The site will need templates for a homepage, global sub-page, and contact page. Interchangeable block elements would be nice if we want to create other templates or change element positions.

Target Market(s)

Continued education and philanthropy individuals/organizations

Industry/Entity Type

Non-profit / college education

Coding

Coded - Design and coding required

Number of Pages Required

3 page

Font styles to use
Sans Serif
Script

Colors
0094D4
00A9DD
6FCCEA
C7EBF8
E9F6FB
59FF00
82FF00
B8FF75
E3FFCB
F4FFEA
FFC000
F8CF3A
FAE287
FDF2CF
FEFAEE
EE7325
F08F49
F5BC92
FAE3D3
FDF4ED
6B429C
8869AF
B7A5CE
E3DAEB
F3F0F8

Requirements
Must have
• Modern responsive design, impactful visual elements, available theme elements pre styled for things like forms, buttoms, tables...
Nice to have
• Onscroll vidual effects, heros with background video

```html
<!DOCTYPE html>
<html lang="en">
<head>
<meta charset="utf-8">
<title>The Harlow Foundation</title>
<link href="https://fonts.googleapis.com/css2?family=Poppins:wght@400;500;600;700&family=Kaushan+Script&display=swap" rel="stylesheet">
<style>
:root{
  --yellow:#f3c632;
  --green:#6fd37a;
  --navy:#2a2b55;
  --ink:#1d1d2c;
  --muted:#777b8a;
  --plum:#2b1f3c;
  --pink:#ee5a7e;
  --orange:#f5a623;
  --teal:#31b6cf;
  --purple:#7a5ec9;
  --line:#e6e6ee;
}
*{margin:0;padding:0;box-sizing:border-box}
html,body{width:1200px;height:5305px;overflow:hidden}
body{position:relative;font-family:"Poppins",sans-serif;color:var(--ink);background:#fff}
.abs{position:absolute}
.btn{position:absolute;display:flex;align-items:center;justify-content:center;background:var(--green);color:#fff;border-radius:24px;font-size:12px;font-weight:600;letter-spacing:.5px;text-transform:uppercase}
.label{position:absolute;left:0;width:1200px;text-align:center;font-size:12px;font-weight:600;color:#9a9cab;letter-spacing:1px;text-transform:uppercase}
.title{position:absolute;left:0;width:1200px;text-align:center;font-size:42px;font-weight:500;color:var(--ink)}
.wave{position:absolute}

/* nav */
.nav{position:absolute;top:0;left:0;width:1200px;height:74px;background:#fff;z-index:3}
.nav .brand{position:absolute;left:86px;top:24px;font-size:19px;font-weight:600}
.nav .burger{position:absolute;left:34px;top:27px}
.nav ul{position:absolute;left:449px;top:29px;display:flex;gap:30px;list-style:none;font-size:11.5px;font-weight:500}
.nav .lang{position:absolute;left:879px;top:28px;font-size:12px;font-weight:600}
.nav .donate{position:absolute;left:967px;top:0;width:233px;height:74px;background:var(--yellow);display:flex;align-items:center;justify-content:center;font-size:13px;font-weight:600}

/* hero */
.hero{position:absolute;top:74px;left:0;width:1200px;height:739px;background:linear-gradient(100deg,#3c2b8e 0%,#5a3aa0 30%,#b2405f 65%,#d2565a 100%)}
.hero h1{position:absolute;left:86px;top:214px;font-size:70px;line-height:77px;font-weight:500;color:#fff}
.hero h1 span{color:var(--yellow)}
.hero p{position:absolute;left:86px;top:385px;width:450px;font-size:15px;line-height:24px;color:#fff}
.hero .thumb{position:absolute;left:996px;top:673px;width:204px;height:126px;background:#fff}
.hero .thumb div{position:absolute;left:10px;top:10px;width:126px;height:116px;background:linear-gradient(135deg,#4a4e60,#9aa0b0)}
.hero .thumb span{position:absolute;left:170px;top:22px;writing-mode:vertical-rl;font-size:9px;font-weight:600;letter-spacing:1px}

/* services */
.service{position:absolute;top:1043px;width:194px;height:217px;background:#fff;box-shadow:0 10px 30px rgba(30,30,60,.08);text-align:center}
.service svg{margin-top:40px}
.service h3{margin-top:18px;font-size:16px;font-weight:500;line-height:22px}

/* about */
.about-text{position:absolute;left:648px;top:1446px;width:470px}
.about-text .kick{font-size:12px;font-weight:600;letter-spacing:1px;color:#9a9cab}
.about-text h2{margin-top:12px;font-size:44px;line-height:50px;font-weight:500}
.about-text p{margin-top:54px;font-size:15px;line-height:24px;color:#555a6b}

/* causes */
.cause{position:absolute;top:2179px;width:362px;height:517px;background:#fff;box-shadow:0 10px 40px rgba(30,30,60,.08)}
.cause h3{position:absolute;left:30px;top:32px;font-size:21px;font-weight:500}
.cause p{position:absolute;left:30px;top:68px;width:305px;font-size:13px;line-height:21px;color:#666}
.cause .img{position:absolute;left:14px;top:134px;width:334px;height:270px}
.cause .tag{position:absolute;left:20px;top:120px;padding:0 16px;height:26px;border-radius:13px;color:#fff;font-size:10px;font-weight:600;display:flex;align-items:center;letter-spacing:.5px;z-index:1}
.cause .pct{position:absolute;left:60px;top:426px;font-size:11px;font-weight:600}
.cause .bar{position:absolute;left:14px;top:452px;width:334px;height:6px;background:var(--line);border-radius:3px}
.cause .bar i{display:block;width:23%;height:100%;background:var(--green);border-radius:3px}
.cause .goal{position:absolute;left:14px;top:476px;width:334px;display:flex;justify-content:space-between;font-size:12px;color:#999}
.cause .goal b{color:var(--ink);font-weight:500}

/* donate band */
.band{position:absolute;top:2807px;left:0;width:1200px;height:595px;background:linear-gradient(90deg,#262850 0%,#2c2e5c 40%,#3e4178 62%,#7b80b4 100%);overflow:hidden}
.band .kick{position:absolute;left:86px;top:124px;font-size:12px;font-weight:600;color:#b8bad5;letter-spacing:1px}
.band h2{position:absolute;left:86px;top:152px;font-size:42px;font-weight:500;color:#fff}
.band .sub{position:absolute;left:86px;top:243px;font-size:13px;font-weight:600;color:#fff}
.band .amount{position:absolute;left:86px;top:272px;font-size:48px;color:#fff}
.band .amount b{font-weight:700}
.band .bar{position:absolute;left:86px;top:355px;width:400px;height:8px;background:#41436e;border-radius:4px}
.band .bar i{display:block;width:51%;height:100%;background:var(--yellow);border-radius:4px}
.band .deco{position:absolute;left:1004px;top:389px;width:215px;height:215px;border-radius:50%;background:rgba(255,255,255,.45)}

/* blog */
.post{position:absolute;top:3610px;width:282px;height:399px;background:#fff;box-shadow:0 10px 30px rgba(30,30,60,.08)}
.post .img{height:218px}
.post .meta{position:absolute;left:27px;top:258px;font-size:11px;color:#666}
.post h3{position:absolute;left:27px;top:282px;width:230px;font-size:19px;line-height:21px;font-weight:600}
.post p{position:absolute;left:27px;top:335px;width:230px;font-size:12.5px;line-height:19px;color:#777}

/* volunteer */
.script{position:absolute;left:0;top:4040px;width:1200px;text-align:center;font-family:"Kaushan Script",cursive;font-size:190px;color:var(--yellow);line-height:1}
.vol-title{position:absolute;left:0;top:4300px;width:1200px;text-align:center;font-size:42px;line-height:50px;font-weight:500}

/* footer */
.footer{position:absolute;top:4846px;left:0;width:1200px;height:459px;background:var(--plum);color:#fff}
.footer .brand{position:absolute;left:86px;top:198px;font-size:36px;line-height:40px;font-weight:600}
.footer h4{font-size:18px;font-weight:600;margin-bottom:22px}
.footer .col{position:absolute;top:84px}
.footer ul{list-style:none;font-size:12px;line-height:31px}
.footer .contact{font-size:12px;line-height:20px}
.footer .contact div{display:flex;gap:10px;margin-bottom:14px}
.footer .news p{font-size:12px;line-height:19px;width:230px}
.footer .field{margin-top:16px;width:259px;height:38px;background:#fff;border-radius:19px;position:relative;color:#777;font-size:12px;padding:11px 0 0 36px}
.footer .field span{position:absolute;right:0;top:0;width:42px;height:38px;border-radius:19px;background:var(--yellow)}
.footer .social{display:flex;gap:10px;margin-top:18px}
.footer .social i{width:32px;height:32px;border-radius:50%;background:#3d3152;display:block}
.footer .copy{position:absolute;left:0;top:418px;width:1200px;text-align:center;font-size:11px;font-weight:500}
.footer .top{position:absolute;left:1134px;top:372px;width:50px;height:50px;border-radius:50%;background:#fff}
</style>
</head>
<body>

<header class="nav">
  <svg class="burger" width="24" height="18"><path d="M0 2h24M0 9h24M0 16h24" stroke="#1d1d2c" stroke-width="2"/></svg>
  <div class="brand">The Harlow Foundation</div>
  <ul><li>SPONSORSHIP</li><li>DONATE</li><li>ABOUT</li><li>EVENTS</li><li>CONTACT</li></ul>
  <div class="lang">ENG ⌄</div>
  <div class="donate">DONATE</div>
</header>

<section class="hero" role="img" aria-label="Smiling child photo with purple and red colour overlay">
  <h1>Our <span>Helping</span><br>around the world</h1>
  <p>We dream about a new world for the children with no harm. We are aiming to build a strong....</p>
  <div class="btn" style="left:86px;top:465px;width:192px;height:48px">Discover more</div>
  <div class="thumb"><div role="img" aria-label="Photo of a child"></div><span>SCROLL DOWN</span></div>
</section>

<div class="label" style="top:926px">Services</div>
<div class="title" style="top:940px">What we do for all people</div>
<svg class="wave" style="left:581px;top:1004px" width="38" height="8"><path d="M1 6l6-4 6 4 6-4 6 4 6-4 6 4" fill="none" stroke="#c9c9d4" stroke-width="2"/></svg>

<div class="service" style="left:191px;border-bottom:3px solid var(--pink)">
  <svg width="64" height="74" viewBox="0 0 64 74" fill="none" stroke="#ee5a7e" stroke-width="2.5"><rect x="16" y="2" width="24" height="8"/><rect x="10" y="10" width="36" height="50" rx="4"/><path d="M22 30h12M28 24v12"/><circle cx="46" cy="54" r="12"/><path d="M38 46l16 16"/></svg>
  <h3>Medicine<br>Help</h3>
</div>
<div class="service" style="left:393px;border-bottom:3px solid var(--orange)">
  <svg width="74" height="74" viewBox="0 0 74 74" fill="none" stroke="#f5a623" stroke-width="2.5"><path d="M8 62L58 12l8 8-50 50H8z"/><path d="M12 12l50 50M12 12l10-6 46 46-6 10"/></svg>
  <h3>We Build and<br>Create</h3>
</div>
<div class="service" style="left:595px;border-bottom:3px solid var(--green)">
  <svg width="74" height="74" viewBox="0 0 74 74" fill="none" stroke="#6fd37a" stroke-width="2.5"><path d="M24 6c-8 14-14 22-14 30a14 14 0 0028 0c0-8-6-16-14-30z"/><path d="M54 30c-5 9-9 14-9 19a9 9 0 0018 0c0-5-4-10-9-19z"/></svg>
  <h3>Water<br>Delivery</h3>
</div>
<div class="service" style="left:798px;border-bottom:3px solid var(--teal)">
  <svg width="74" height="74" viewBox="0 0 74 74" fill="none" stroke="#31b6cf" stroke-width="2.5"><circle cx="37" cy="30" r="24"/><path d="M13 30h48M37 6c10 12 10 36 0 48M37 6c-10 12-10 36 0 48"/><path d="M8 58c10-4 18 4 28 4h20"/></svg>
  <h3>We Care<br>About</h3>
</div>

<div class="abs" style="left:0;top:1373px;width:282px;height:55px;background:var(--yellow)"></div>
<div class="abs" role="img" aria-label="Group photo of scholarship students in front of a brick building" style="left:0;top:1428px;width:566px;height:441px;background:linear-gradient(160deg,#b88a74,#8d6a5e 45%,#3e3540)"></div>
<div class="abs" style="left:0;top:1869px;width:282px;height:55px;background:var(--yellow)"></div>
<div class="abs" role="img" aria-label="Small decorative dot accent" style="left:528px;top:1834px;width:70px;height:90px;background:#ececf2"></div>

<div class="about-text">
  <div class="kick">ABOUT US</div>
  <h2>The harlow foundation history</h2>
  <svg class="wave" style="left:0;top:134px" width="38" height="8"><path d="M1 6l6-4 6 4 6-4 6 4 6-4 6 4" fill="none" stroke="#c9c9d4" stroke-width="2"/></svg>
  <p>The Harlow Foundation was founded from Martin and Clara Harlow's vision to design an innovative program that would dramatically increase the graduation rates of first-generation college students—those who are first in their family to attend college. For several years prior to starting the foundation, the Harlows endowed scholarships at Northfield State University and Eastbrook University...</p>
</div>
<div class="btn" style="left:648px;top:1805px;width:146px;height:43px">Learn more</div>

<div class="abs" role="img" aria-label="Soft purple watercolour splash" style="left:960px;top:1840px;width:300px;height:340px;border-radius:50%;background:radial-gradient(circle,rgba(183,165,206,.5),rgba(227,218,235,.15) 65%,transparent 72%)"></div>
<div class="abs" style="left:810px;top:2066px;width:36px;height:36px;border-radius:50%;background:#c9c0ef"></div>

<div class="label" style="top:2048px">What we do</div>
<div class="title" style="top:2062px">Harlow Causes</div>
<svg class="wave" style="left:581px;top:2126px" width="38" height="8"><path d="M1 6l6-4 6 4 6-4 6 4 6-4 6 4" fill="none" stroke="#c9c9d4" stroke-width="2"/></svg>

<div class="cause" style="left:86px">
  <h3>Some heading here</h3>
  <p>The Harlow Foundation was founded from Martin and Clara Harlow's vision to design</p>
  <span class="tag" style="background:var(--pink)">FOOD</span>
  <div class="img" role="img" aria-label="Women receiving food aid sacks in a village" style="background:linear-gradient(135deg,#9a7c63,#6a5448 50%,#c9c2bd)"></div>
  <div class="pct">23%</div><div class="bar"><i></i></div>
  <div class="goal"><span>Goals: <b>14 000$</b></span><span>Pledged: <b>6 098$</b></span></div>
</div>
<div class="cause" style="left:475px">
  <h3>Some heading here</h3>
  <p>The Harlow Foundation was founded from Martin and Clara Harlow's vision to design</p>
  <span class="tag" style="background:var(--orange)">EDUCATION</span>
  <div class="img" role="img" aria-label="Group of smiling schoolchildren" style="background:linear-gradient(135deg,#6b4a3c,#a27a62 50%,#4a3630)"></div>
  <div class="pct">23%</div><div class="bar"><i></i></div>
  <div class="goal"><span>Goals: <b>14 000$</b></span><span>Pledged: <b>6 098$</b></span></div>
</div>
<div class="cause" style="left:862px">
  <h3>Some heading here</h3>
  <p>The Harlow Foundation was founded from Martin and Clara Harlow's vision to design</p>
  <span class="tag" style="background:#7fb0e0">MEDICINE</span>
  <div class="img" role="img" aria-label="Women in colourful clothing at a community gathering" style="background:linear-gradient(135deg,#b26a48,#7d4d3e 50%,#c28a5a)"></div>
  <div class="pct">23%</div><div class="bar"><i></i></div>
  <div class="goal"><span>Goals: <b>14 000$</b></span><span>Pledged: <b>6 098$</b></span></div>
</div>

<section class="band">
  <div class="abs" role="img" aria-label="Close-up photo of a child looking upward, blue toned" style="left:560px;top:0;width:640px;height:595px;background:radial-gradient(ellipse at 65% 40%,#8e92c2,#4c5088 55%,transparent 80%)"></div>
  <div class="kick">DONATE</div>
  <h2>We are very thankful</h2>
  <svg class="wave" style="left:86px;top:210px" width="38" height="8"><path d="M1 6l6-4 6 4 6-4 6 4 6-4 6 4" fill="none" stroke="#6a6c94" stroke-width="2"/></svg>
  <div class="sub">You've helped us arise an overwhelming</div>
  <div class="amount"><b>$12,370,743</b> so far!</div>
  <div class="bar"><i></i></div>
  <div class="btn" style="left:88px;top:410px;width:190px;height:49px">Donate now</div>
  <div class="deco" role="img" aria-label="Decorative striped circle accent"></div>
</section>

<div class="label" style="top:3486px">Blog</div>
<div class="title" style="top:3502px">Upcoming event</div>
<svg class="wave" style="left:581px;top:3566px" width="38" height="8"><path d="M1 6l6-4 6 4 6-4 6 4 6-4 6 4" fill="none" stroke="#c9c9d4" stroke-width="2"/></svg>

<div class="post" style="left:161px">
  <div class="img" role="img" aria-label="Children reading at a school desk" style="background:linear-gradient(135deg,#3f4a5a,#7a6c63)"></div>
  <div class="meta">byJohn &nbsp;•&nbsp; January 2021</div>
  <h3>Stay up to date with latest news.</h3>
  <p>Aenean sollicitudin bibendum is a auctor, nisi elit consequat...</p>
</div>
<div class="post" style="left:457px">
  <div class="img" role="img" aria-label="Classroom full of children raising hands" style="background:linear-gradient(135deg,#6d5a4e,#b59a86)"></div>
  <div class="meta">byJohn &nbsp;•&nbsp; January 2021</div>
  <h3>Stay up to date with latest news.</h3>
  <p>Aenean sollicitudin bibendum is a auctor, nisi elit consequat...</p>
</div>
<div class="post" style="left:755px">
  <div class="img" role="img" aria-label="Smiling boy with a backpack" style="background:linear-gradient(135deg,#c9894a,#5a3b2c)"></div>
  <div class="meta">byJohn &nbsp;•&nbsp; January 2021</div>
  <h3>Stay up to date with latest news.</h3>
  <p>Aenean sollicitudin bibendum is a auctor, nisi elit consequat...</p>
</div>

<div class="script">Volunteer</div>
<div class="vol-title">Delivering help and hope<br>to children through sponsorship</div>
<svg class="wave" style="left:581px;top:4400px" width="38" height="8"><path d="M1 6l6-4 6 4 6-4 6 4 6-4 6 4" fill="none" stroke="#c9c9d4" stroke-width="2"/></svg>
<div class="btn" style="left:482px;top:4437px;width:234px;height:45px">Become a volunteer</div>
<div class="abs" role="img" aria-label="Group of smiling volunteers in blue shirts" style="left:0;top:4486px;width:1200px;height:360px;background:linear-gradient(180deg,#ffffff 0%,#8fd3e6 30%,#2ba7c8 70%,#1a7e9c 100%)"></div>

<footer class="footer">
  <div class="brand">The Harlow<br>Foundation</div>
  <div class="col" style="left:403px">
    <h4>Information</h4>
    <ul><li>FAQ</li><li>Privacy Policy</li><li>Terms of use</li><li>Support</li><li>Regulations</li><li>Site Map</li></ul>
  </div>
  <div class="col contact" style="left:599px">
    <h4>Contact Info</h4>
    <div><svg width="12" height="10"><rect x="0.5" y="0.5" width="11" height="9" fill="none" stroke="#f3c632"/><path d="M1 1l5 4 5-4" fill="none" stroke="#f3c632"/></svg><span>Email:<br>hello@harlowfund.org</span></div>
    <div><svg width="12" height="12"><path d="M2 1l3 0 1 3-2 1c1 2 2 3 4 4l1-2 3 1v3c-6 0-10-4-10-10z" fill="#f3c632"/></svg><span>Phone:<br>+1 555 014 2290</span></div>
    <div><svg width="10" height="14"><path d="M5 14C1 8 0 6 0 5a5 5 0 0110 0c0 1-1 3-5 9z" fill="#f3c632"/></svg><span>Office Location:<br>Some address line goes here<br>city name...</span></div>
  </div>
  <div class="col news" style="left:854px">
    <h4>Newsletter</h4>
    <p>Subscribe to our email address to get the latest news.</p>
    <div class="field">Enter Your Email...<span></span></div>
    <div class="social"><i></i><i></i><i></i></div>
  </div>
  <div class="top"></div>
  <div class="copy">COPYRIGHT 2021 © THE HARLOW FOUNDATION. ALL RIGHT RESERVED</div>
</footer>

</body>
</html>
```